Startup photography business has a new logo, now we need business cards

Design a business card for the two partners of our business.
Our business Brisk Pelican has a new logo and we need to design a business card to showcase it and us.
Our colours of blue and orange are punchy and vivid, but how can we make the most of it on our card?

It should have our name Brisk Pelican
name of partner
phone number
email
website

Industry/Entity Type

Professional Photography

Contact Information for Business Card

Tom Ashworth
+61 400 55 61 72
tom@briskpelican.com.au
briskpelican.com.au

second card
Neil Porter
+61 400 918 263
neil@briskpelican.com.au
briskpelican.com.au

Colors
f37122
f68d4c
33a6d7
0592cd

Requirements
Must have
• one version of our logo, we have included options
• Name
• phone number
• email
• website
Nice to have
• instagram briskpelicanmedia
• twitter briskpelicanmedia
• facebook briskpelicanmedia

```html
<!DOCTYPE html>
<html lang="en">
<head>
<meta charset="utf-8">
<title>Brisk Pelican – Business Card</title>
<link rel="stylesheet" href="https://fonts.googleapis.com/css2?family=Russo+One&family=Roboto:wght@400;500&display=swap">
<style>
  :root {
    --brand-orange: #f37122;
    --brand-orange-light: #f68d4c;
    --ink: #0d0d0d;
    --ink-soft: #3a3a3a;
    --paper: #ffffff;
    --backdrop: #e9e6e1;
    --card-w: 360px;
    --card-h: 600px;
  }
  * { box-sizing: border-box; margin: 0; padding: 0; }
  html, body {
    width: 1200px;
    height: 1023px;
    overflow: hidden;
    background: var(--backdrop);
  }
  .stage {
    position: relative;
    width: 1200px;
    height: 1023px;
    display: flex;
    align-items: center;
    justify-content: center;
    gap: 120px;
  }
  .card {
    position: relative;
    width: var(--card-w);
    height: var(--card-h);
    overflow: hidden;
    box-shadow: 0 10px 30px rgba(0,0,0,0.18);
  }
  .card--front { background: var(--brand-orange); }
  .card--back { background: var(--paper); }

  .top-band {
    position: absolute;
    top: 0;
    left: 22px;
    right: 0;
    height: 40px;
    background: var(--ink);
    border-radius: 0 0 0 26px;
  }
  .bottom-band {
    position: absolute;
    bottom: 0;
    left: 0;
    width: 84%;
    height: 44px;
    border-radius: 0 26px 0 0;
  }
  .card--front .bottom-band { background: var(--paper); }
  .card--back .bottom-band {
    left: auto;
    right: 0;
    width: 90%;
    background: var(--brand-orange);
    border-radius: 26px 0 0 0;
  }

  .brand {
    position: absolute;
    left: 50%;
    top: 50%;
    transform: translate(-50%, -50%) rotate(-90deg);
    display: flex;
    align-items: center;
    gap: 18px;
    white-space: nowrap;
  }
  .brand__mark {
    width: 34px;
    height: 34px;
    background: var(--paper);
  }
  .brand__name {
    font-family: "Russo One", sans-serif;
    font-size: 40px;
    letter-spacing: 1px;
    text-transform: uppercase;
    color: var(--paper);
  }

  .contact {
    position: absolute;
    left: 40px;
    right: 30px;
    top: 50%;
    transform: translateY(-50%);
  }
  .contact__name {
    font-family: "Russo One", sans-serif;
    font-size: 30px;
    line-height: 1.15;
    text-transform: uppercase;
    color: var(--ink);
  }
  .contact__rule {
    width: 60px;
    height: 5px;
    margin: 16px 0 26px;
    background: var(--brand-orange);
    border-radius: 3px;
  }
  .contact__list { list-style: none; }
  .contact__item {
    display: flex;
    align-items: center;
    gap: 14px;
    margin-bottom: 18px;
    font-family: "Roboto", sans-serif;
    font-size: 17px;
    font-weight: 500;
    color: var(--ink-soft);
    white-space: nowrap;
  }
  .contact__icon {
    flex: none;
    width: 30px;
    height: 30px;
    border-radius: 50%;
    background: var(--brand-orange);
    display: flex;
    align-items: center;
    justify-content: center;
  }
  .contact__icon svg { width: 16px; height: 16px; }
</style>
</head>
<body>
  <main class="stage">
    <section class="card card--front" aria-label="Business card front">
      <div class="top-band"></div>
      <div class="brand">
        <span class="brand__mark"></span>
        <span class="brand__name">Brisk Pelican</span>
      </div>
      <div class="bottom-band"></div>
    </section>

    <section class="card card--back" aria-label="Business card back">
      <div class="top-band"></div>
      <div class="contact">
        <h1 class="contact__name">Tom Ashworth</h1>
        <div class="contact__rule"></div>
        <ul class="contact__list">
          <li class="contact__item">
            <span class="contact__icon">
              <svg viewBox="0 0 24 24" fill="#fff"><path d="M6.6 10.8a15.1 15.1 0 0 0 6.6 6.6l2.2-2.2c.3-.3.7-.4 1-.2 1.1.4 2.3.6 3.6.6.6 0 1 .4 1 1V20c0 .6-.4 1-1 1A17 17 0 0 1 3 4c0-.6.4-1 1-1h3.5c.6 0 1 .4 1 1 0 1.3.2 2.5.6 3.6.1.3 0 .7-.2 1z"/></svg>
            </span>
            +61 400 55 61 72
          </li>
          <li class="contact__item">
            <span class="contact__icon">
              <svg viewBox="0 0 24 24" fill="none" stroke="#fff" stroke-width="2.2"><rect x="3" y="5" width="18" height="14" rx="2"/><path d="M3 7l9 6 9-6"/></svg>
            </span>
            tom@briskpelican.com.au
          </li>
          <li class="contact__item">
            <span class="contact__icon">
              <svg viewBox="0 0 24 24" fill="none" stroke="#fff" stroke-width="2"><circle cx="12" cy="12" r="9"/><path d="M3 12h18M12 3c2.5 2.8 2.5 15.2 0 18M12 3c-2.5 2.8-2.5 15.2 0 18"/></svg>
            </span>
            briskpelican.com.au
          </li>
        </ul>
      </div>
      <div class="bottom-band"></div>
    </section>
  </main>
</body>
</html>
```